Contemporary Media Company with Logo Needs Business Card Design

Need a modern card design for a full service digital media company using the logo included. Also want the info below on the card. Probably list the services on the card back to save space for the front. Want something contemporary to impress prospective clients. You may want to submit both a somewhat more conservative design, and then a more wild one.
General Info: (this phrase need not be on the card)
Ned Parlow
Founder and CEO
949-612-4830
ned@vontaramedia.example
vontaramedia.example
Services: (this word need not be on the card)
Content & Experience Strategy
Brand Development
Search Engine Optimization
Website Design
Website Operation
Social Media Integration
Complete Video Solutions
Updates
Industry/Entity Type
Business
Contact Information for Business Card
Ned Parlow
Founder and CEO
949-612-4830
ned@vontaramedia.example
vontaramedia.example
Brand Development
Website Design
Website Operation
Social Media Integration
Complete Video Solutions
Look and feel
Each slider illustrates characteristics of the customer's brand and the style your logo design should communicate.

```html
<!DOCTYPE html>
<html lang="en">
<head>
<meta charset="utf-8">
<title>Vontara Media – Business Card</title>
<link href="https://fonts.googleapis.com/css2?family=Open+Sans:wght@400;600;700&display=swap" rel="stylesheet">
<style>
  :root {
    --backdrop: #ececec;
    --card-dark: #2a2a2a;
    --card-dark-soft: #3a3a3a;
    --card-light: #f7f8f8;
    --accent: #f7941d;
    --accent-deep: #f26b1d;
    --ink: #4a4a4a;
    --ink-soft: #6d6d6d;
    --on-dark: #d9d9d9;
    --on-dark-soft: #a8a8a8;
    --logo-grey: #9a9a9a;
  }
  * { margin: 0; padding: 0; box-sizing: border-box; }
  html, body {
    width: 1200px; height: 1039px; overflow: hidden;
    background: radial-gradient(ellipse at 50% 45%, #f6f6f6 0%, var(--backdrop) 70%);
    font-family: "Open Sans", Arial, sans-serif;
  }
  .stage { position: relative; width: 1200px; height: 1039px; }
  .card {
    position: absolute; top: 365px;
    width: 540px; height: 309px;
    border-radius: 22px; overflow: hidden;
    box-shadow: 0 10px 26px rgba(0,0,0,0.22);
  }
  .card--front { left: 45px; }
  .card--back {
    left: 615px;
    background: linear-gradient(135deg, var(--card-dark-soft) 0%, var(--card-dark) 55%, #1f1f1f 100%);
  }
  .card__art { position: absolute; inset: 0; width: 100%; height: 100%; }

  .holder { position: absolute; left: 42px; top: 96px; }
  .holder__name { font-size: 24px; font-weight: 600; color: var(--ink); line-height: 1; }
  .holder__title { font-size: 11px; font-weight: 600; color: var(--ink-soft); margin-top: 5px; }
  .holder__address {
    position: absolute; left: 42px; top: 170px;
    font-size: 14px; color: var(--ink-soft); line-height: 1.35;
  }
  .contact {
    position: absolute; right: 22px; top: 88px;
    text-align: right; font-size: 11px; color: var(--on-dark); line-height: 1.6;
  }
  .website {
    position: absolute; left: 42px; bottom: 20px;
    font-size: 14px; color: var(--on-dark); letter-spacing: 0.3px;
  }

  .brand {
    position: absolute; left: 50%; top: 128px;
    transform: translate(-50%, -50%);
    display: flex; align-items: center; gap: 16px;
  }
  .brand__mark { width: 30px; height: 30px; background: var(--accent-deep); }
  .brand__name {
    font-size: 30px; font-weight: 600; color: var(--logo-grey);
    letter-spacing: 4px; white-space: nowrap;
  }
  .services {
    position: absolute; left: 40px; right: 40px; bottom: 34px;
    list-style: none; text-align: center;
    font-size: 11px; color: var(--on-dark-soft); line-height: 1.8;
  }
  .services li { display: inline; }
  .services li + li::before { content: "•"; color: var(--accent-deep); margin: 0 8px; }
</style>
</head>
<body>
<main class="stage">

  <section class="card card--front" aria-label="Business card front">
    <svg class="card__art" viewBox="0 0 540 309" preserveAspectRatio="none" aria-hidden="true">
      <defs>
        <linearGradient id="darkFace" x1="0" y1="0" x2="1" y2="1">
          <stop offset="0" stop-color="#3b3b3b"/>
          <stop offset="1" stop-color="#1e1e1e"/>
        </linearGradient>
        <linearGradient id="swoosh" x1="0" y1="0" x2="1" y2="0">
          <stop offset="0" stop-color="#f7a23a"/>
          <stop offset="1" stop-color="#f26b1d"/>
        </linearGradient>
      </defs>
      <rect width="540" height="309" fill="url(#darkFace)"/>
      <path d="M385 0 H420 C405 175 285 255 0 268 V246 C255 232 368 150 385 0 Z" fill="url(#swoosh)"/>
      <path d="M0 0 H385 C368 150 255 232 0 246 Z" fill="#f7f8f8"/>
      <path d="M420 0 H428 C412 180 292 262 0 276 V268 C285 255 405 175 420 0 Z" fill="#555"/>
    </svg>
    <div class="holder">
      <p class="holder__name">Ned Parlow</p>
      <p class="holder__title">Founder and CEO</p>
    </div>
    <p class="holder__address">Address line1, Address line2,<br>City, Zipcode</p>
    <div class="contact">
      <p>Mobile 949-612-4830</p>
      <p>Telephone 949-612-4830</p>
      <p>ned@vontaramedia.example</p>
    </div>
    <p class="website">www.vontaramedia.example</p>
  </section>

  <section class="card card--back" aria-label="Business card back">
    <div class="brand">
      <span class="brand__mark"></span>
      <span class="brand__name">VONTARA MEDIA</span>
    </div>
    <ul class="services">
      <li>Content &amp; Experience Strategy</li><li>Brand Development</li><li>Search Engine Optimization</li><li>Website Design</li><li>Website Operation</li><li>Social Media Integration</li><li>Complete Video Solutions</li>
    </ul>
  </section>

</main>
</body>
</html>
```